Letterhead Design Project - Real Estate Development Company

I need a letterhead design for a real estate development company. I have utilized Pixel Harbor for my company logo, as well as our business cards and have had good success so far. I will attach those files so that elements from those designs can be utilized in the letterhead design so there is fluidity within our brand. We develop commercial real estate in the southeast United States for national retailers such as Thrift Corner, Kestner Motor Supply, etc. I would like the letterhead to have a professional feel to it. It will be sent to existing clients, potential clients and landowners. If possible, I would like a design for the first page of the letterhead with logo, contact info, etc., and then a second page design I would use for subsequent pages in the letters I send to clients. I envision the second page design to be a stripped down version of the main letterhead design and would most likely exclude our contact info. I would prefer the design to be created in InDesign as I have that software. Also, if the design can be easily transferred to Microsoft Word that would be a plus as I often need to send letters electronically (printing a Word document to PDF). If possible, I would like to have a matching envelope created too.

Target Market(s)

Target market will be real estate managers and executives (of national companies), as well as landowners. Age - 30 to 65. College educated.

Industry/Entity Type

Real Estate

Requirements
Must have
• Our logo (attached)

Our address/Contact Info:
5716 Tillow Court
Calloway Springs, Florida 34620
Office Phone - 863.571.6204
Fax - 863.571.9482

Nice to have
• My partners and I really like the back of our business card which is blue with a white and blue MV logo. Might be nice to incorporate this element somehow. And to take that further, maybe take our entire logo (not just the "MV" as is on the business card), make it white, and put it on a blue background similar to what is on the back of the business card.

If possible, I would like to have a matching envelope created too.

```html
<!DOCTYPE html>
<html lang="en">
<head>
<meta charset="utf-8">
<title>Harlowe Crest Development Letterhead</title>
<link href="https://fonts.googleapis.com/css2?family=Tinos:wght@400;700&display=swap" rel="stylesheet">
<style>
  :root {
    --brand-navy: #014a7f;
    --brand-blue: #2f6ea5;
    --brand-sky: #8fb4d6;
    --paper: #ffffff;
    --rule: #5a5a5a;
    --ink: #111111;
  }
  html, body {
    margin: 0;
    padding: 0;
    overflow: hidden;
    background: var(--paper);
  }
  .letterhead {
    position: relative;
    width: 927px;
    height: 1200px;
    background: var(--paper);
    overflow: hidden;
    font-family: "Tinos", "Times New Roman", serif;
  }
  .header-band {
    position: absolute;
    top: 0;
    left: 0;
    width: 100%;
    height: 205px;
    background: linear-gradient(
      to bottom,
      var(--brand-navy) 0%,
      var(--brand-blue) 40%,
      var(--brand-sky) 72%,
      var(--paper) 100%
    );
  }
  .brand-name {
    position: absolute;
    top: 44px;
    left: 0;
    width: 100%;
    margin: 0;
    text-align: center;
    color: var(--paper);
    font-family: "Tinos", "Times New Roman", serif;
    font-weight: 400;
    font-size: 56px;
    letter-spacing: 1px;
    line-height: 1;
  }
  .footer-rule {
    position: absolute;
    left: 0;
    top: 1110px;
    width: 100%;
    height: 0;
    border-top: 1.5px solid var(--rule);
  }
  .contact-block {
    position: absolute;
    top: 1122px;
    left: 0;
    width: 100%;
    margin: 0;
    text-align: center;
    font-style: normal;
    font-weight: 700;
    font-size: 14px;
    line-height: 16px;
    color: var(--ink);
  }
  .contact-block span {
    display: block;
  }
</style>
</head>
<body>
  <main class="letterhead">
    <header class="header-band">
      <h1 class="brand-name">Harlowe Crest Development</h1>
    </header>

    <div class="footer-rule"></div>
    <address class="contact-block">
      <span class="contact-street">5716 Tillow Court</span>
      <span class="contact-city">Calloway Springs, Florida 34620</span>
      <span class="contact-phone">Office Phone: 863-571-6204</span>
      <span class="contact-fax">Fax: 863-571-9482</span>
    </address>
  </main>
</body>
</html>
```